Corvane Capital LLC
I need single sided standard sized Business Card [3.5" x 2"]
Fonts to be determined by designer
Professional
Derek Halloway
Chairman
Kestrel Hall Tower
418 North Larkin Avenue
Los Angeles, CA 90099
555.014.2739 X1
Acquisitions@Corvane-Capital.net
http://www.Corvane-Capital.net
We want to see what designs are out there for a cutting edge business card that shows off our 3 main goals: Intense - Expressive - Important . The business card can be vertical or horizontal, can use fonts of the designer's choice and be relatively "unique". More than just a simple black on white business card.
Use the logo and CORVANE but you do not need to use the blue background if your design does not warrant it. Financial LLC can be in any font you desire if it matches your design

```html
<!DOCTYPE html>
<html lang="en">
<head>
<meta charset="utf-8">
<title>Corvane Capital LLC — Business Card</title>
<link rel="stylesheet" href="https://fonts.googleapis.com/css2?family=Arimo:ital,wght@0,400;1,400&display=swap">
<style>
  :root {
    --backdrop: #3a3d40;
    --card: #ffffff;
    --gold-light: #e8c77a;
    --gold-mid: #c9963b;
    --gold-dark: #8a5f1c;
    --mark: #b58a45;
    --ink: #1c1c1c;
    --ink-soft: #333333;
  }
  * { margin: 0; padding: 0; box-sizing: border-box; }
  html, body {
    width: 1200px;
    height: 751px;
    overflow: hidden;
    background: var(--backdrop);
    font-family: "Arimo", Arial, sans-serif;
  }
  .business-card {
    position: absolute;
    left: 271px;
    top: 185px;
    width: 660px;
    height: 379px;
    background: var(--card);
    border-radius: 16px;
    overflow: hidden;
    box-shadow: 0 8px 24px rgba(0,0,0,0.35);
  }
  .gold-band {
    position: absolute;
    left: 0;
    width: 100%;
    background: linear-gradient(90deg, var(--gold-dark) 0%, var(--gold-light) 35%, var(--gold-mid) 65%, var(--gold-dark) 100%);
  }
  .gold-band--top { top: 0; height: 9px; }
  .gold-band--bottom { bottom: 0; height: 15px; }

  .brand-lockup {
    position: absolute;
    left: 30px;
    top: 74px;
    width: 290px;
    display: flex;
    flex-direction: column;
    align-items: center;
  }
  .brand-square {
    width: 118px;
    height: 118px;
    background: var(--mark);
  }
  .brand-name {
    margin-top: 30px;
    font-size: 26px;
    font-weight: 400;
    color: var(--ink);
    white-space: nowrap;
  }

  .holder {
    position: absolute;
    left: 365px;
    top: 30px;
  }
  .holder-name {
    font-style: italic;
    font-weight: 400;
    font-size: 32px;
    color: var(--ink);
    line-height: 1.1;
  }
  .holder-title {
    font-style: italic;
    font-weight: 400;
    font-size: 19px;
    color: var(--ink-soft);
    margin-top: 4px;
  }

  .contact {
    position: absolute;
    left: 365px;
    top: 222px;
    font-size: 15px;
    line-height: 18.5px;
    color: var(--ink-soft);
    list-style: none;
  }
</style>
</head>
<body>
  <article class="business-card">
    <div class="gold-band gold-band--top"></div>

    <div class="brand-lockup">
      <div class="brand-square"></div>
      <div class="brand-name">Corvane Capital LLC</div>
    </div>

    <header class="holder">
      <h1 class="holder-name">Derek Halloway</h1>
      <p class="holder-title">Chairman</p>
    </header>

    <ul class="contact">
      <li>Kestrel Hall Tower</li>
      <li>418 North Larkin Avenue</li>
      <li>Los Angeles, CA 90099</li>
      <li>P: 555.014.2739</li>
      <li>F: 555.014.2740</li>
      <li>E: Acquisitions@Corvane-Capital.net</li>
      <li>W: www.Corvane-Capital.net</li>
    </ul>

    <div class="gold-band gold-band--bottom"></div>
  </article>
</body>
</html>
```